Business cards/stationary for physician office
Using existing logo
Bright & Fun-filled
Paul Verner, M.D.
Radiologist
Cedarpoint Imaging, LLC.
48 Quill Ridge Lane
Montgomery, TX 77490
office@brakwell-mail.net
www.cedarpointimaging-demo.com
Will contact the winning designer with actual contact info to replace above text. Please not website has not been updated with new logo, so make sure to use provided logo files.
Logo files
Logo file horizontal

```html
<!DOCTYPE html>
<html lang="en">
<head>
<meta charset="utf-8">
<title>Cedarpoint Imaging Stationery</title>
<link href="https://fonts.googleapis.com/css2?family=Lato:wght@400;700&display=swap" rel="stylesheet">
<style>
:root{
  --bg:#2a2a2b;
  --paper:#ffffff;
  --blue:#2b5896;
  --blue-dark:#1d3f70;
  --grey:#c9cbce;
  --grey-light:#eceef0;
  --ink:#3b3f46;
  --label:#9a9a9a;
}
*{margin:0;padding:0;box-sizing:border-box}
html,body{width:1200px;height:382px;overflow:hidden;background:var(--bg);font-family:"Lato",sans-serif;color:var(--ink)}
.board{position:relative;width:1200px;height:382px}
.abs{position:absolute}
.brand{display:flex;align-items:center;gap:8px}
.brand-dot{border-radius:50%;background:var(--blue);flex:none}
.brand-name{font-weight:700;letter-spacing:.06em;text-transform:uppercase;color:var(--blue);line-height:1.05}
.hero-brand{left:58px;top:80px}
.hero-brand .brand-dot{width:48px;height:48px;background:var(--grey-light)}
.hero-brand .brand-name{font-size:22px;color:var(--paper)}
.card{width:127px;height:56px;background:var(--paper);overflow:hidden}
.card-front{display:flex;align-items:center;justify-content:center}
.card-front .brand-dot{width:14px;height:14px}
.card-front .brand-name{font-size:8px}
.card-front.is-blue{background:var(--blue)}
.card-front.is-blue .brand-dot{background:var(--paper)}
.card-front.is-blue .brand-name{color:var(--paper)}
.card-back .band{position:absolute;left:0;right:0;bottom:0;height:16px;background:var(--blue)}
.card-back .person{position:absolute;right:8px;top:7px;text-align:right}
.person-name{font-size:6px;font-weight:700;color:var(--blue)}
.person-role{font-size:4.5px}
.card-back .contact{position:absolute;right:8px;top:22px;text-align:right;font-size:3.6px;line-height:1.35}
.card-back .band-text{position:absolute;left:8px;bottom:5px;font-size:4px;color:var(--paper)}
.label{font-size:6px;color:var(--label);text-align:center}
.letterhead{width:200px;height:295px;background:var(--paper);overflow:hidden}
.letterhead .brand{position:absolute;left:14px;top:14px;gap:5px}
.letterhead .brand-dot{width:16px;height:16px}
.letterhead .brand-name{font-size:7px}
.letterhead .contact{position:absolute;right:14px;top:13px;text-align:right;font-size:3.6px;line-height:1.4}
.watermark{position:absolute;left:50%;top:110px;width:96px;height:96px;margin-left:-48px;border-radius:50%;background:var(--grey-light)}
.wave{position:absolute;left:0;bottom:0;width:200px;height:48px}
.envelope{width:384px;background:var(--paper);overflow:hidden}
.envelope .brand{position:absolute;left:16px;top:12px;gap:5px}
.envelope .brand-dot{width:16px;height:16px}
.envelope .brand-name{font-size:7px}
.envelope .address{position:absolute;left:16px;top:34px;font-size:4px;line-height:1.4}
.envelope .flap{position:absolute;left:0;top:0;width:100%;height:100%}
.envelope .band{position:absolute;left:0;right:0;bottom:0;height:14px;background:var(--blue)}
</style>
</head>
<body>
<div class="board">

  <div class="abs brand hero-brand">
    <span class="brand-dot"></span>
    <span class="brand-name">Cedarpoint<br>Imaging</span>
  </div>

  <!-- business cards -->
  <div class="abs card card-front" style="left:12px;top:163px">
    <div class="brand"><span class="brand-dot"></span><span class="brand-name">Cedarpoint<br>Imaging</span></div>
  </div>
  <div class="abs label" style="left:12px;top:222px;width:127px">Card Front A</div>

  <div class="abs card card-back" style="left:144px;top:163px">
    <div class="person"><div class="person-name">Paul Verner, M.D.</div><div class="person-role">Radiologist</div></div>
    <div class="contact">Tel 936.555.0140<br>Fax 936.555.0141<br>office@brakwell-mail.net</div>
    <div class="band"></div>
    <div class="band-text">www.cedarpointimaging-demo.com</div>
  </div>
  <div class="abs label" style="left:144px;top:222px;width:127px">Card Back A</div>

  <div class="abs card card-front is-blue" style="left:12px;top:247px">
    <div class="brand"><span class="brand-dot"></span><span class="brand-name">Cedarpoint<br>Imaging</span></div>
  </div>
  <div class="abs label" style="left:12px;top:306px;width:127px">Card Front B</div>

  <div class="abs card card-back" style="left:144px;top:247px">
    <div class="person"><div class="person-name">Paul Verner, M.D.</div><div class="person-role">Radiologist</div></div>
    <div class="contact">Tel 936.555.0140<br>Fax 936.555.0141<br>48 Quill Ridge Lane, Montgomery, TX 77490</div>
    <div class="band"></div>
    <div class="band-text">www.cedarpointimaging-demo.com</div>
  </div>
  <div class="abs label" style="left:144px;top:306px;width:127px">Card Back B</div>

  <!-- letterheads -->
  <div class="abs letterhead" style="left:312px;top:41px">
    <div class="brand"><span class="brand-dot"></span><span class="brand-name">Cedarpoint<br>Imaging</span></div>
    <div class="contact">48 Quill Ridge Lane<br>Montgomery, TX 77490<br>Tel 936.555.0140</div>
    <div class="watermark"></div>
    <svg class="wave" viewBox="0 0 200 48" preserveAspectRatio="none" aria-hidden="true">
      <path d="M0 22 C60 40 130 8 200 20 L200 48 L0 48Z" fill="var(--grey)"/>
      <path d="M0 30 C60 46 130 16 200 28 L200 48 L0 48Z" fill="var(--blue)"/>
    </svg>
  </div>
  <div class="abs label" style="left:312px;top:345px;width:200px">CedarpointImaging_01_17526.ai</div>

  <div class="abs letterhead" style="left:533px;top:41px">
    <div class="brand"><span class="brand-dot"></span><span class="brand-name">Cedarpoint<br>Imaging</span></div>
    <div class="contact">office@brakwell-mail.net<br>www.cedarpointimaging-demo.com<br>Fax 936.555.0141</div>
    <div class="watermark"></div>
    <svg class="wave" viewBox="0 0 200 48" preserveAspectRatio="none" aria-hidden="true">
      <path d="M0 22 C60 40 130 8 200 20 L200 48 L0 48Z" fill="var(--grey)"/>
      <path d="M0 30 C60 46 130 16 200 28 L200 48 L0 48Z" fill="var(--blue)"/>
    </svg>
  </div>
  <div class="abs label" style="left:533px;top:345px;width:200px">CedarpointImaging_02_17527.ai</div>

  <!-- envelopes -->
  <div class="abs envelope" style="left:792px;top:41px;height:104px">
    <svg class="flap" viewBox="0 0 384 104" preserveAspectRatio="none" aria-hidden="true">
      <path d="M0 0 L384 0 L384 18 L192 62 L0 18Z" fill="var(--grey)"/>
    </svg>
  </div>

  <div class="abs envelope" style="left:792px;top:152px;height:92px">
    <div class="brand"><span class="brand-dot"></span><span class="brand-name">Cedarpoint<br>Imaging</span></div>
    <div class="address">48 Quill Ridge Lane<br>Montgomery, TX 77490</div>
    <div class="band"></div>
  </div>

  <div class="abs envelope" style="left:792px;top:252px;height:92px">
    <div class="brand"><span class="brand-dot"></span><span class="brand-name">Cedarpoint<br>Imaging</span></div>
    <div class="address">48 Quill Ridge Lane<br>Montgomery, TX 77490</div>
    <div class="band"></div>
  </div>

</div>
</body>
</html>
```